Stationery set created from logo

Existing logo design from successful designer K72. Thanks K72.

We now now need letterhead, business card design and background slide for powerpoint presentations. These need to be provided as PDF; JPEG and AI files.

I also need the names of the fonts used and the RGB colour/PMS colour names

Thankyou for submitting your designs. A design has been selcted. I appreciate youtr work. God wishes to you

```html
<!DOCTYPE html>
<html lang="en">
<head>
<meta charset="utf-8">
<title>NCMA Letterhead</title>
<link href="https://fonts.googleapis.com/css2?family=Arimo:wght@400;700&display=swap" rel="stylesheet">
<style>
  :root {
    --band-deep: #0a5ea6;
    --band-mid: #1a78c4;
    --band-light: #4aa3e6;
    --ribbon-white: #ffffff;
    --ribbon-shade: #e4edf6;
    --navy: #1b2a6b;
    --body-blue: #1666ad;
    --ghost: rgba(22, 102, 173, 0.05);
    --page: #ffffff;
  }
  html, body {
    margin: 0;
    padding: 0;
    width: 848px;
    height: 1200px;
    overflow: hidden;
    background: var(--page);
  }
  .letterhead {
    position: relative;
    width: 848px;
    height: 1200px;
    background: var(--page);
    font-family: "Arimo", Arial, sans-serif;
    overflow: hidden;
  }
  .header-band {
    position: absolute;
    top: 0;
    left: 0;
    width: 848px;
    height: 180px;
  }
  .ribbon {
    position: absolute;
    top: 0;
    left: 327px;
    width: 200px;
    height: 168px;
  }
  .ribbon-brand {
    position: absolute;
    top: 62px;
    left: 327px;
    width: 200px;
    text-align: center;
  }
  .brand-name {
    font-weight: 700;
    font-size: 40px;
    letter-spacing: 2px;
    color: var(--navy);
    line-height: 1;
  }
  .ghost-name {
    position: absolute;
    top: 824px;
    left: 0;
    width: 848px;
    text-align: center;
    white-space: nowrap;
    font-weight: 700;
    font-size: 26px;
    letter-spacing: 3px;
    color: var(--ghost);
  }
  .ghost-strip {
    position: absolute;
    top: 870px;
    left: 0;
    width: 848px;
    height: 36px;
    background: var(--ghost);
  }
  .letter-body {
    position: absolute;
    top: 316px;
    left: 67px;
    width: 722px;
    color: var(--body-blue);
    font-size: 20.4px;
    line-height: 25px;
  }
  .letter-body p {
    margin: 0 0 25px;
  }
  .footer-brand {
    position: absolute;
    top: 1108px;
    left: 53px;
    width: 146px;
    text-align: center;
  }
  .footer-brand .brand-name {
    font-size: 32px;
  }
</style>
</head>
<body>
<main class="letterhead">
  <svg class="header-band" viewBox="0 0 848 180" aria-hidden="true">
    <path d="M0 0 H848 V128 C700 150 560 92 420 112 C260 135 140 120 0 78 Z" fill="var(--band-light)"/>
    <path d="M0 0 H848 V118 C700 140 560 84 420 104 C260 126 140 110 0 70 Z" fill="var(--band-mid)"/>
    <path d="M0 0 H848 V104 C700 124 560 72 420 92 C260 112 140 96 0 58 Z" fill="var(--band-deep)"/>
  </svg>

  <svg class="ribbon" viewBox="0 0 200 168" aria-hidden="true">
    <path d="M0 0 H200 V164 L100 138 L0 164 Z" fill="var(--band-mid)"/>
    <path d="M3 0 H197 V156 L100 131 L3 156 Z" fill="var(--ribbon-white)"/>
    <path d="M3 118 H197 V156 L100 131 L3 156 Z" fill="var(--ribbon-shade)"/>
  </svg>
  <div class="ribbon-brand">
    <div class="brand-name">NCMA</div>
  </div>

  <div class="ghost-strip" aria-hidden="true"></div>
  <div class="ghost-name" aria-hidden="true">NORTHFIELD CLINICAL MENTORS ALLIANCE</div>

  <article class="letter-body">
    <p>Lorem ipsum dolor sit amet, consectetur adipiscing elit. Sed non risus. Suspendisse lectus tortor, dignissim sit amet, adipiscing nec, ultricies sed, dolor. Cras elementum ultrices diam. Maecenas ligula massa, varius a</p>
    <p>semper congue, euismod non, mi. Proin porttitor, orci nec nonummy molestie, enim est eleifend mi, non fermentum diam nisl sit amet erat. Duis semper. Duis arcu massa, scelerisque vitae, consequat in, pretium a, enim. Pellentesque congue. Ut in risus volutpat libero pharetra tempor. Cras</p>
    <p>vestibulum bibendum augue. Praesent egestas leo in pede. Praesent blandit odio eu enim. Pellentesque sed dui ut augue blandit sodales. Vestibulum ante ipsum primis in faucibus orci luctus et ultrices posuere cubilia Curae; Aliquam nibh. Mauris ac mauris sed pede pellentesque fermentum. Maecenas adipiscing ante non diam sodales hendrerit. Pst canata tari est paroy malardi dalr sahit ya kho ral labass erat non mauris convallis vehicula. Nulla et sapien. Integer tortor tellus, aliquam faucibus, convallis id, congue eu, quam. Mauris ullamcorper felis vitae erat. Proin feugiat, augue non elementum posuere, metus purus iaculis lectus, et tristique ligula justo vitae magna. Aliquam convallis sollicitudin purus. Praesent aliquam, enim at fermentum mollis, ligula massa adipiscing nisl, ac euismod nibh nisl eu lectus. Fusce vulputate sem at sapien. Vivamus leo. Aliquam euismod libero eu enim. Nulla nec felis sed leo placerat imperdiet. Aenean suscipit nulla in justo. Suspendisse cursus rutrum augue. Nulla tincidunt tincidunt mi. Curabitur iaculis, lorem vel rhoncus faucibus, felis magna fermentum augue, et ultricies lacus lorem varius purus. Curabitur eu amet.</p>
  </article>

  <footer class="footer-brand">
    <div class="brand-name">NCMA</div>
  </footer>
</main>
</body>
</html>
```